Training Materials Cover design

Graphic design for the front and back cover of a training manual. Review my website at www.gvtrmx.com. The business name is Meridale Academy of Trade Praxis

Target Market(s)

Professional people and those interested in professional and personal development

Requirements
Must have
• Front and back cover. Should include my current logo. The front page title should be 'Venture Steward of Praxis'

```html
<!DOCTYPE html>
<html lang="en">
<head>
<meta charset="utf-8">
<title>Venture Steward of Praxis – Manual Covers</title>
<link href="https://fonts.googleapis.com/css2?family=Montserrat:wght@400;600;700&display=swap" rel="stylesheet">
<style>
  :root {
    --stage: #545454;
    --navy: #27467a;
    --navy-deep: #1f3a68;
    --green: #17842f;
    --white: #ffffff;
    --photo-warm: #8a6f5e;
    --photo-cool: #c9ccd2;
  }
  html, body {
    margin: 0;
    padding: 0;
    width: 1200px;
    height: 1200px;
    overflow: hidden;
    background: var(--stage);
  }
  .stage {
    display: block;
    width: 1200px;
    height: 1200px;
    font-family: "Montserrat", sans-serif;
  }
  .cover-title { font-weight: 700; font-size: 50px; fill: var(--white); }
  .cover-url { font-weight: 400; font-size: 14px; letter-spacing: 2px; fill: var(--white); }
  .crest-name { font-weight: 600; fill: var(--green); }
  .back-quote { font-weight: 400; font-size: 13.5px; fill: var(--white); }
  .back-quote .emphasis { font-weight: 700; }
</style>
</head>
<body>
<svg class="stage" viewBox="0 0 1500 1500" xmlns="http://www.w3.org/2000/svg">
  <defs>
    <linearGradient id="coverBg" x1="0" y1="0" x2="1" y2="1">
      <stop offset="0" stop-color="#2a4b80"/>
      <stop offset="1" stop-color="#223f6f"/>
    </linearGradient>
    <linearGradient id="photoWarm" x1="0" y1="0" x2="0" y2="1">
      <stop offset="0" stop-color="#b07a5f"/>
      <stop offset="0.45" stop-color="#d9d6d2"/>
      <stop offset="1" stop-color="#4a3a34"/>
    </linearGradient>
    <linearGradient id="photoCrowd" x1="0" y1="0" x2="1" y2="1">
      <stop offset="0" stop-color="#9a7a66"/>
      <stop offset="0.5" stop-color="#5b4338"/>
      <stop offset="1" stop-color="#2d2a33"/>
    </linearGradient>
    <linearGradient id="photoOffice" x1="0" y1="0" x2="1" y2="1">
      <stop offset="0" stop-color="#e7e8ea"/>
      <stop offset="1" stop-color="#c3c7cf"/>
    </linearGradient>
    <clipPath id="frontClip"><rect x="50" y="277" width="678" height="951"/></clipPath>
    <clipPath id="backClip"><rect x="762" y="280" width="675" height="948"/></clipPath>
    <filter id="panelShadow" x="-10%" y="-10%" width="120%" height="120%">
      <feDropShadow dx="0" dy="6" stdDeviation="8" flood-color="#000" flood-opacity="0.45"/>
    </filter>
  </defs>

  <!-- Front cover -->
  <g class="front-cover">
    <rect x="50" y="277" width="678" height="951" fill="url(#coverBg)" filter="url(#panelShadow)"/>
    <g clip-path="url(#frontClip)">
      <circle class="photo-ring" cx="600" cy="795" r="425" fill="var(--navy-deep)"/>
      <circle class="hero-photo" cx="600" cy="795" r="365" fill="url(#photoWarm)" stroke="var(--white)" stroke-width="3"
              role="img" aria-label="Photo: a presenter speaking to a seated audience in a brick-walled training room"/>
      <circle class="title-disc" cx="245" cy="800" r="205" fill="var(--green)"/>
    </g>
    <g class="crest">
      <circle cx="197" cy="592" r="85" fill="var(--white)"/>
      <text class="crest-name" text-anchor="middle" font-size="15">
        <tspan x="197" y="575">Meridale</tspan>
        <tspan x="197" y="596">Academy of</tspan>
        <tspan x="197" y="617">Trade Praxis</tspan>
      </text>
    </g>
    <text class="cover-title">
      <tspan x="98" y="765">Venture</tspan>
      <tspan x="98" y="818">Steward</tspan>
      <tspan x="98" y="871">of Praxis</tspan>
    </text>
    <text class="cover-url" x="108" y="909">www.gvtrmx.com</text>
  </g>

  <!-- Back cover -->
  <g class="back-cover">
    <rect x="762" y="280" width="675" height="948" fill="url(#coverBg)" filter="url(#panelShadow)"/>
    <g clip-path="url(#backClip)">
      <circle class="photo-ring" cx="955" cy="560" r="410" fill="var(--navy-deep)"/>
      <circle class="hero-photo" cx="955" cy="560" r="368" fill="url(#photoCrowd)" stroke="var(--white)" stroke-width="3"
              role="img" aria-label="Photo: a smiling participant raising her hand in a seated workshop group"/>
      <circle class="corner-disc" cx="1430" cy="310" r="95" fill="var(--green)"/>
      <circle class="corner-disc" cx="822" cy="1182" r="125" fill="var(--green)"/>
    </g>
    <g class="inset-photo">
      <circle cx="1193" cy="793" r="188" fill="var(--green)"/>
      <circle cx="1193" cy="793" r="172" fill="var(--white)"/>
      <circle cx="1193" cy="793" r="165" fill="url(#photoOffice)"
              role="img" aria-label="Photo: a woman in glasses gesturing as she speaks at a meeting table"/>
    </g>
    <g class="crest">
      <circle cx="1255" cy="1055" r="50" fill="var(--white)" stroke="var(--green)" stroke-width="2"/>
      <text class="crest-name" text-anchor="middle" font-size="9.5">
        <tspan x="1255" y="1045">Meridale</tspan>
        <tspan x="1255" y="1058">Academy of</tspan>
        <tspan x="1255" y="1071">Trade Praxis</tspan>
      </text>
    </g>
    <text class="back-quote" text-anchor="middle">
      <tspan x="1264" y="1129">The only way you or any person you are</tspan>
      <tspan x="1264" y="1145">trying to work with will experience is from</tspan>
      <tspan x="1264" y="1161">your <tspan class="emphasis">practice, practice, practice</tspan>.</tspan>
    </text>
    <text class="cover-url" x="1265" y="1191" text-anchor="middle" font-size="13">www.gvtrmx.com</text>
  </g>
</svg>
</body>
</html>
```